Landing page for Dunmore Aviation

Re-design the landing page for www.dunmoreaviation-example.com. It needs to be flatter and work with both PC, Mac and Mobile. Sites I like are as follows:
http://kravelaero-example.com
http://zuvair-example.com
http://www.skyvantor-example.com
http://www.bralojet-example.com/bjc.php
http://www.qwing-example.com
http://www.tolvenair-example.com
http://www.merrowfieldaerohub-example.com
http://www.corvexwings-example.com
http://www.stratovelfield-example.com

We are a Durnell 48 Dealer, SkyVesta FBO member, Kestrin Circle FBO, TQN Preferred FBO located only 6 miles from Downtown Atlanta. Providing Aircraft charter, Aircraft sales, Aircraft Maintenance, Aircraft Line Services and Hangar, and Parts Support.
Updates

Project Deadline Extended
Reason: I have six people reviewing designs within the company and will not be able to complete the review until next week.

Target Market(s)

Pilot's looking for a place to take care of them in Atlanta

Industry/Entity Type

Group

Colors
fbed22
0555a3

Requirements
Must have
• Slogan "Focused on Arrival" and "Sensational Southern Service"

```html
<!DOCTYPE html>
<html lang="en">
<head>
<meta charset="utf-8">
<title>Dunmore Aviation – Focused on Arrival</title>
<link rel="stylesheet" href="https://fonts.googleapis.com/css2?family=Arimo:wght@400;700&family=Mulish:wght@400&family=Play:wght@400;700&family=Oswald:wght@600&family=Chewy&display=swap">
<style>
:root{
  --yellow:#fbed22;
  --blue:#0555a3;
  --navy:#0c2553;
  --navy-deep:#061a40;
  --sky:#bfe9f3;
  --sky-pale:#e8f8fb;
  --ink:#333;
  --grey-bg:#f1f1f1;
  --white:#fff;
}
*{box-sizing:border-box;margin:0;padding:0}
html,body{width:1029px;height:1200px;overflow:hidden}
body{background:var(--grey-bg);font-family:"Mulish",sans-serif;color:var(--ink);position:relative}

.site-header{position:absolute;left:0;top:0;width:1029px;height:114px;
  background:linear-gradient(100deg,var(--sky-pale) 0%,var(--sky) 45%,#9fe0ee 70%,var(--sky-pale) 100%)}
.brand{position:absolute;left:116px;top:34px;display:flex;align-items:center;gap:10px}
.brand-mark{width:30px;height:30px;background:var(--blue)}
.brand-name{font-family:"Play",sans-serif;font-weight:700;font-size:26px;color:var(--blue)}

.world-clocks{position:absolute;left:324px;top:8px;display:flex;gap:0;list-style:none}
.world-clocks li{font-family:"Play",sans-serif;font-size:11px;color:#111;text-align:center;margin-right:27px}
.world-clocks .flag{display:inline-block;width:12px;height:8px;background:linear-gradient(#c33 0 50%,#2a4f9e 50%);margin-right:2px;vertical-align:0}
.world-clocks .time{display:block;color:var(--blue);letter-spacing:.5px;margin-top:2px}

.social{position:absolute;left:824px;top:3px;display:flex;gap:4px}
.social span{width:26px;height:26px;border-radius:50%;background:#3f68b6}
.social span:last-child{background:#4fb3e6}

.main-nav{position:absolute;left:0;top:114px;width:1029px;height:28px;background:var(--blue)}
.main-nav ul{list-style:none;display:flex;margin-left:116px;height:28px}
.main-nav li{font-family:"Arimo",sans-serif;font-size:12.5px;color:var(--white);padding:0 7px;line-height:28px;border-right:1px solid #3a7cc0}
.main-nav li:last-child{border-right:0}

.hero{position:absolute;left:0;top:142px;width:1029px;height:232px;background:var(--yellow)}
.hero-photo{position:absolute;left:116px;top:2px;width:797px;height:230px;
  background:linear-gradient(#5d9ad9 0%,#a9cbe9 45%,#d8dde3 58%,#8a8f95 72%,#6d7176 100%)}
.hero-slogan{position:absolute;left:148px;top:10px;font-family:"Chewy",cursive;font-size:29px;line-height:33px;color:var(--yellow);
  text-shadow:1px 1px 0 #555,-1px -1px 0 #555,1px -1px 0 #555,-1px 1px 0 #555}

.intro-band{position:absolute;left:0;top:374px;width:1029px;height:40px;background:linear-gradient(#cfe7f7,var(--grey-bg))}
.intro{position:absolute;left:116px;top:402px;width:797px;font-size:10.5px;line-height:15.5px;color:#222}
.intro p+p{margin-top:15px}

.services{position:absolute;left:126px;top:548px;display:flex;gap:19px;list-style:none}
.service{width:180px;height:213px;background:var(--white);border-top:4px solid var(--blue);position:relative;box-shadow:0 2px 4px rgba(0,0,0,.08)}
.service h2{font-family:"Play",sans-serif;font-weight:400;font-size:16px;line-height:17px;color:var(--blue);text-align:center;height:44px;display:flex;align-items:center;justify-content:center;letter-spacing:.5px}
.service .photo{height:86px;border-top:2px solid var(--yellow);border-bottom:2px solid var(--yellow)}
.service p{font-size:10px;line-height:15px;text-align:center;color:#444;padding:8px 14px 0}
.read-more{position:absolute;left:35px;bottom:-10px;width:110px;height:28px;background:var(--yellow);border-bottom:3px solid #c9bd12;
  font-family:"Oswald",sans-serif;font-weight:600;font-size:15px;letter-spacing:1.5px;color:#333;text-align:center;line-height:26px;border-radius:2px}

.partners{position:absolute;left:116px;top:803px;width:797px;height:125px;background:var(--white)}
.partners .arrow{position:absolute;top:42px}
.partner-list{position:absolute;left:39px;top:30px;display:flex;gap:9px;list-style:none}
.partner-list li{height:67px;border:2px solid var(--yellow);display:flex;align-items:center;justify-content:center;
  font-family:"Play",sans-serif;font-weight:700;font-size:18px;color:var(--blue)}

.site-footer{position:absolute;left:0;top:957px;width:1029px;height:214px;
  background:radial-gradient(ellipse 420px 160px at 420px 60px,#1d5ea8 0%,#0f3f86 40%,transparent 75%),linear-gradient(90deg,var(--navy-deep),var(--navy) 50%,var(--navy-deep))}
.footer-nav{position:absolute;left:116px;top:34px;list-style:none}
.footer-nav li{font-family:"Arimo",sans-serif;font-size:12px;line-height:17.2px;color:var(--white)}
.anniversary{position:absolute;left:430px;top:63px;width:169px;height:91px;border:3px solid var(--yellow);background:linear-gradient(#f7f7f7,#dfe9f3)}
.contact{position:absolute;left:722px;top:34px;color:var(--white);font-family:"Arimo",sans-serif}
.contact h3{font-size:13.5px;font-weight:700;margin-bottom:14px}
.contact .row{display:flex;gap:10px;font-size:12px;line-height:17px;margin-bottom:6px}
.contact .row svg{flex:none;margin-top:2px}
.contact .indent{padding-left:22px}

.copyright{position:absolute;left:0;top:1171px;width:1029px;height:29px;background:var(--yellow);text-align:center;
  font-family:"Play",sans-serif;font-size:10px;line-height:29px;color:#222}
</style>
</head>
<body>

<header class="site-header">
  <div class="brand"><span class="brand-mark"></span><span class="brand-name">Dunmore Aviation</span></div>
  <ul class="world-clocks">
    <li><span class="flag"></span>Atlanta<span class="time">03:01:10</span></li>
    <li><span class="flag"></span>GMT<span class="time">03:01:10</span></li>
    <li><span class="flag"></span>San Francisco<span class="time">03:01:10</span></li>
    <li><span class="flag"></span>Salt Lake<span class="time">03:01:10</span></li>
    <li><span class="flag"></span>Dallas<span class="time">03:01:10</span></li>
    <li><span class="flag"></span>London<span class="time">03:01:10</span></li>
  </ul>
  <div class="social" role="img" aria-label="Social network links"><span></span><span></span><span></span></div>
</header>

<nav class="main-nav">
  <ul>
    <li>Home</li><li>About Us</li><li>Aircraft Management</li><li>Charter</li><li>FBO Services</li>
    <li>Maintenance</li><li>Aircraft Parts</li><li>Aircraft Sales</li><li>Resources</li><li>Contact Us</li>
  </ul>
</nav>

<section class="hero">
  <div class="hero-photo" role="img" aria-label="White business jet parked on the ramp beside a hangar"></div>
  <h1 class="hero-slogan">Focused on Arrival<br>Sensational Southern Service</h1>
</section>

<div class="intro-band"></div>
<section class="intro">
  <p>Atlanta's Most Established Fixed Based Operation established in 1955 by Peachline Aviation Hall of Fame member Walter Dunmore, Sr.<br>
  Our world class FBO facilities offer all the amenities for passengers and pilots, including computer work stations with internet access, plasma TV for catching up on national and world events, pilots lounge with theatre seating and security camera monitors and state of the art flight planning facilities. Our line technicians are ALSA Safety First trained and Dunmore Aviation is a State of Georgia recognized drug-free workplace.</p>
  <p>Our concierge services can take care of passenger and crew ground transportation, hotel reservations and catering, we can even arrange for sporting event tickets or a round of golf. Let Dunmore Aviation show you why we have been named the #1 FBO in Georgia multiple times. Experience our "Sensational Southern Service".</p>
</section>

<ul class="services">
  <li class="service">
    <h2>AIRCRAFT CHARTER</h2>
    <div class="photo" role="img" aria-label="Charter jet parked outside a terminal" style="background:linear-gradient(#8a7b62,#c9c2b4 55%,#7d7a74)"></div>
    <p>Our charter desk flies you anywhere on your own schedule...</p>
    <span class="read-more">READ MORE</span>
  </li>
  <li class="service">
    <h2>JET MANAGEMENT<br>TURNKEY PROGRAM</h2>
    <div class="photo" role="img" aria-label="Managed aircraft inside a hangar" style="background:linear-gradient(#2f4f6e,#7d98ad 55%,#b9c2c8)"></div>
    <p>Dunmore Aviation offers a full range of aircraft management services.</p>
    <span class="read-more">READ MORE</span>
  </li>
  <li class="service">
    <h2>LINE SERVICES</h2>
    <div class="photo" role="img" aria-label="Line technician fueling an aircraft" style="background:linear-gradient(#6f9fd0,#b8cfe3 45%,#8b96a2)"></div>
    <p>Including Fueling and storage, Aircraft Maintenance ...</p>
    <span class="read-more">READ MORE</span>
  </li>
  <li class="service">
    <h2>AIRCRAFT SALES</h2>
    <div class="photo" role="img" aria-label="Turboprop aircraft for sale in a hangar" style="background:linear-gradient(#5f7488,#c8ced4 50%,#5c6a7a)"></div>
    <p>Including Jet, Turboprop, and Single Engine Aircraft...</p>
    <span class="read-more">READ MORE</span>
  </li>
</ul>

<section class="partners">
  <svg class="arrow" style="left:4px" width="26" height="36" viewBox="0 0 26 36" aria-label="Previous"><path d="M22 2 6 18l16 16" fill="none" stroke="var(--blue)" stroke-width="6"/></svg>
  <ul class="partner-list">
    <li style="width:160px">Durnell 48</li>
    <li style="width:110px">SkyVesta</li>
    <li style="width:110px">Ferrox Fuel</li>
    <li style="width:148px">TQN</li>
    <li style="width:140px">Rendal</li>
  </ul>
  <svg class="arrow" style="left:767px" width="26" height="36" viewBox="0 0 26 36" aria-label="Next"><path d="M4 2l16 16L4 34" fill="none" stroke="var(--blue)" stroke-width="6"/></svg>
</section>

<footer class="site-footer">
  <ul class="footer-nav">
    <li>Home</li><li>About Us</li><li>Aircraft Management</li><li>Charter</li><li>FBO Services</li>
    <li>Maintenance</li><li>Aircraft Parts</li><li>Aircraft Sales</li><li>Resources</li><li>Contact Us</li>
  </ul>
  <div class="anniversary" role="img" aria-label="50th anniversary celebration banner"></div>
  <address class="contact" style="font-style:normal">
    <h3>Dunmore Aviation and Leasing Corp.</h3>
    <div class="row">
      <svg width="12" height="16" viewBox="0 0 12 16"><path d="M6 0a6 6 0 0 0-6 6c0 4.5 6 10 6 10s6-5.5 6-10a6 6 0 0 0-6-6z" fill="var(--yellow)"/><circle cx="6" cy="6" r="2.3" fill="var(--navy)"/></svg>
      <span>1200 Example Field Road<br>Atlanta, GA 30300</span>
    </div>
    <div class="row" style="margin-top:8px">
      <svg width="12" height="12" viewBox="0 0 12 12"><path d="M1 4c0-2 2-3 5-3s5 1 5 3H8V3H4v1zM2 5h8l1 6H1z" fill="var(--yellow)"/></svg>
      <span>555-010-3330</span>
    </div>
    <div class="row indent" style="margin-top:6px">555-010-8305</div>
    <div class="row" style="margin-top:12px">
      <svg width="12" height="12" viewBox="0 0 12 12"><rect x="3" y="0" width="6" height="4" fill="var(--yellow)"/><rect x="0" y="4" width="12" height="6" rx="1" fill="var(--yellow)"/><rect x="3" y="8" width="6" height="4" fill="var(--yellow)" stroke="var(--navy)"/></svg>
      <span>555-010-1446</span>
    </div>
  </address>
</footer>

<div class="copyright">Copyright © 2007-2014 Dunmore Aviation &amp; Leasing &nbsp;|&nbsp; All rights reserved</div>

</body>
</html>
```